7 variations of an already existing packet design needed

i need 8 colour and flavour variations of a design that i have already in AI/PDF/PSD format

i need 7 colour variations of the packet with the names of the flavours incorporated onto the packaging itself.

the 7 colour/flavour variations i want are

pineapple
cherry
blueberry
bubblegum
strawberry
menthol
mango
Apple & Blackcurrant

Requirements
Must have
• Must use the original design and have different colour anf flavour variations as described in the brief.
Should not have
• Not be an original design

```html
<!DOCTYPE html>
<html lang="en">
<head>
<meta charset="utf-8">
<title>Crown Hollow – Flavour Range</title>
<link rel="stylesheet" href="https://fonts.googleapis.com/css2?family=Archivo:wght@800&family=Nunito+Sans:wght@400&display=swap">
<style>
  :root {
    --page-bg: #ffffff;
    --menthol: #2fb58c;
    --menthol-bg: #030a05;
    --menthol-smoke: rgba(40, 110, 60, 0.22);
    --mango: #f28a4a;
    --mango-bg: #0b0907;
    --mango-smoke: rgba(120, 80, 50, 0.18);
    --apple: #c3272f;
    --apple-bg: #0b0202;
    --apple-smoke: rgba(140, 20, 20, 0.22);
    --caption: #6a6a6a;
  }
  html, body {
    margin: 0;
    padding: 0;
    width: 1200px;
    height: 1000px;
    overflow: hidden;
    background: var(--page-bg);
  }
  .range {
    position: relative;
    width: 1200px;
    height: 1000px;
  }
  .packet {
    position: absolute;
    top: 192px;
    width: 351px;
    height: 371px;
    box-shadow: 5px 5px 7px rgba(0, 0, 0, 0.35);
    overflow: hidden;
    text-align: center;
  }
  .packet--menthol { left: 48px;  background: var(--menthol-bg); --accent: var(--menthol); --smoke: var(--menthol-smoke); }
  .packet--mango   { left: 424px; background: var(--mango-bg);   --accent: var(--mango);   --smoke: var(--mango-smoke); }
  .packet--apple   { left: 799px; background: var(--apple-bg);   --accent: var(--apple);   --smoke: var(--apple-smoke); }

  .packet__smoke {
    position: absolute;
    inset: 0;
    background:
      radial-gradient(ellipse 60px 260px at 25% 35%, var(--smoke), transparent 70%),
      radial-gradient(ellipse 45px 220px at 60% 25%, var(--smoke), transparent 70%);
  }
  .packet__brand {
    position: absolute;
    left: 0;
    right: 0;
    top: 140px;
    margin: 0;
    font-family: "Archivo", sans-serif;
    font-weight: 800;
    font-size: 30px;
    line-height: 1;
    letter-spacing: 1px;
    color: var(--accent);
    text-transform: uppercase;
  }
  .packet__label {
    position: absolute;
    left: 0;
    right: 0;
    top: 260px;
  }
  .packet__flavour {
    margin: 0;
    font-family: "Archivo", sans-serif;
    font-weight: 800;
    font-size: 14px;
    line-height: 18px;
    color: var(--accent);
    text-transform: uppercase;
  }
  .packet__type {
    margin: 0;
    font-family: "Nunito Sans", sans-serif;
    font-size: 10.5px;
    line-height: 14px;
    color: var(--caption);
  }
</style>
</head>
<body>
<main class="range">
  <section class="packet packet--menthol">
    <div class="packet__smoke" role="img" aria-label="Faint green smoke wisps"></div>
    <h2 class="packet__brand">Crown Hollow</h2>
    <div class="packet__label">
      <p class="packet__flavour">Menthol</p>
      <p class="packet__type">flavoured tobacco</p>
    </div>
  </section>

  <section class="packet packet--mango">
    <div class="packet__smoke" role="img" aria-label="Faint amber smoke wisps"></div>
    <h2 class="packet__brand">Crown Hollow</h2>
    <div class="packet__label">
      <p class="packet__flavour">Mango</p>
      <p class="packet__type">flavoured tobacco</p>
    </div>
  </section>

  <section class="packet packet--apple">
    <div class="packet__smoke" role="img" aria-label="Faint red smoke wisps"></div>
    <h2 class="packet__brand">Crown Hollow</h2>
    <div class="packet__label">
      <p class="packet__flavour">Apple<br>&amp; Blackcurrant</p>
      <p class="packet__type">flavoured tobacco</p>
    </div>
  </section>
</main>
</body>
</html>
```